Pediatric Dental Practice needs a postcard for direct mail advertising

We are looking for a creative and professional double-sided postcard design for a direct mail marketing campaign. Our goal is to attract new families to our pediatric dental practice by conveying a sense of warmth, modern care, and clinical excellence. The design should feel "boutique" and high-end yet remain fun and approachable for parents and children.

```html
<!DOCTYPE html>
<html lang="en">
<head>
<meta charset="utf-8">
<title>maple grove Pediatric Dentistry – Postcard</title>
<link rel="stylesheet" href="https://fonts.googleapis.com/css2?family=Fira+Sans:wght@500;600&family=Open+Sans:wght@300;400&display=swap">
<style>
  :root {
    --ink: #3a3a3a;
    --paper: #ffffff;
    --cream: #f3e6b4;
    --panel-start: #d6d48c;
    --panel-end: #6eaf58;
    --contact-green: #8ecb8e;
    --badge-ring-a: #d9d39a;
    --badge-ring-b: #a9c98a;
    --icon-green: #3f9a55;
    --rule: #8c8670;
  }
  * { margin: 0; padding: 0; box-sizing: border-box; }
  html, body { width: 878px; height: 1200px; overflow: hidden; background: var(--paper); }
  body { position: relative; font-family: "Open Sans", sans-serif; color: var(--ink); }

  .card { position: absolute; left: 78px; width: 723px; height: 516px; overflow: hidden; }
  .card--front { top: 70px; }
  .card--back { top: 615px; background: var(--cream); }

  .front-photo {
    position: absolute; inset: 0;
    background:
      linear-gradient(160deg, rgba(0,0,0,0) 55%, rgba(46,150,150,0.95) 56%, #4fa3a0 100%),
      radial-gradient(circle at 85% 85%, #fbe39a 0%, #f2d98d 30%, rgba(242,217,141,0) 60%),
      linear-gradient(100deg, #d8e3a2 0%, #e3e6a6 30%, #efe0a0 60%, #f5dc95 100%);
  }

  .brand { position: absolute; text-align: center; color: var(--ink); }
  .brand__mark { display: block; width: 40px; height: 40px; margin: 0 auto 6px; border-radius: 50%; background: var(--ink); }
  .brand__name { font-family: "Open Sans", sans-serif; font-weight: 400; font-size: 21px; line-height: 1; letter-spacing: 0.5px; }
  .brand__tag { font-family: "Open Sans", sans-serif; font-weight: 400; font-size: 7px; letter-spacing: 2.6px; margin-top: 4px; }
  .card--front .brand { left: 28px; top: 108px; width: 122px; }
  .card--back .brand { left: 20px; top: 30px; width: 122px; }

  .hero-panel {
    position: absolute; left: 217px; top: 0; width: 488px; height: 393px;
    border-radius: 0 0 22px 22px;
    background: linear-gradient(100deg, var(--panel-start) 0%, #b6c77a 55%, var(--panel-end) 100%);
  }
  .hero-panel__title {
    position: absolute; left: 0; right: 0; top: 62px; text-align: center;
    font-family: "Fira Sans", sans-serif; font-weight: 600; font-size: 58px; line-height: 54px; color: var(--ink);
  }
  .hero-panel__lead {
    position: absolute; left: 0; right: 0; top: 190px; text-align: center;
    font-weight: 300; font-size: 22px; line-height: 25px; color: var(--ink);
  }
  .feature {
    position: absolute; top: 290px; width: 119px; height: 71px;
    background: var(--paper); border-radius: 6px;
    display: flex; align-items: flex-end; justify-content: center; padding-bottom: 8px;
    text-align: center; font-weight: 400; font-size: 16px; line-height: 17px; color: var(--ink);
  }
  .feature--gentle { left: 30px; }
  .feature--tech { left: 181px; }
  .feature--kids { left: 332px; }
  .feature--gentle { padding-bottom: 24px; }
  .feature__badge {
    position: absolute; left: 50%; top: -33px; width: 53px; height: 53px; margin-left: -26.5px;
    border-radius: 50%; background: var(--paper); border: 4px solid var(--badge-ring-a);
  }
  .feature--kids .feature__badge, .feature--tech .feature__badge { border-color: var(--badge-ring-b); }

  .intro { position: absolute; left: 28px; top: 155px; width: 330px; }
  .intro__heading { font-family: "Fira Sans", sans-serif; font-weight: 500; font-size: 17.5px; line-height: 22px; letter-spacing: 0.3px; margin-bottom: 16px; }
  .intro__text { font-weight: 300; font-size: 13.4px; line-height: 16.5px; margin-bottom: 11px; }

  .address-block { position: absolute; left: 40px; top: 358px; width: 300px; }
  .address-block__label { font-family: "Fira Sans", sans-serif; font-weight: 500; font-size: 17px; margin-left: 0; }
  .address-block__line { height: 0; border-top: 1px solid var(--rule); margin-top: 31px; }
  .address-block__line:first-of-type { margin-top: 24px; }

  .contact { position: absolute; left: 376px; top: 22px; width: 325px; height: 172px; background: var(--contact-green); padding: 15px 0 0 26px; }
  .contact__row { display: flex; align-items: flex-start; font-weight: 300; font-size: 14.3px; line-height: 17px; height: 33px; }
  .contact__row svg { flex: 0 0 18px; width: 18px; height: 18px; margin-right: 11px; fill: var(--ink); }
  .contact__row--addr { height: auto; }
  .map { position: absolute; left: 376px; top: 194px; width: 325px; height: 299px;
    background: linear-gradient(135deg, #c7f0d6 0%, #eeeeee 35%, #f0eeee 60%, #bfe9cc 100%); }
</style>
</head>
<body>
  <section class="card card--front">
    <div class="front-photo" role="img" aria-label="Bright pediatric treatment room with a teal dental chair, overhead lamp and colourful seats"></div>
    <div class="brand">
      <span class="brand__mark"></span>
      <div class="brand__name">maple grove</div>
      <div class="brand__tag">PEDIATRIC DENTISTRY</div>
    </div>
    <div class="hero-panel">
      <h1 class="hero-panel__title">Little Smiles<br>Big Care</h1>
      <p class="hero-panel__lead">Where every child feels safe, happy,<br>and excited to smile.</p>
      <div class="feature feature--gentle"><span class="feature__badge"></span>Gentle Care</div>
      <div class="feature feature--tech"><span class="feature__badge"></span>Modern<br>Technology</div>
      <div class="feature feature--kids"><span class="feature__badge"></span>Kid-Friendly<br>Environment</div>
    </div>
  </section>

  <section class="card card--back">
    <div class="brand">
      <span class="brand__mark"></span>
      <div class="brand__name">maple grove</div>
      <div class="brand__tag">PEDIATRIC DENTISTRY</div>
    </div>
    <div class="intro">
      <h2 class="intro__heading">A BOUTIQUE DENTAL EXPERIENCE<br>FOR YOUR CHILD</h2>
      <p class="intro__text">At Dr. Elena Ward, we combine advanced pediatric dentistry with a calm, nurturing environment to make every visit a positive one.</p>
      <p class="intro__text">From first check-ups to preventive and restorative care, our team is dedicated to helping your child build healthy habits—and confident smiles—for life.</p>
    </div>
    <div class="address-block">
      <div class="address-block__label">To</div>
      <div class="address-block__line"></div>
      <div class="address-block__line"></div>
      <div class="address-block__line"></div>
      <div class="address-block__line"></div>
    </div>
    <div class="contact">
      <div class="contact__row">
        <svg viewBox="0 0 24 24"><path d="M6.6 10.8a15.1 15.1 0 0 0 6.6 6.6l2.2-2.2a1 1 0 0 1 1-.25 11.4 11.4 0 0 0 3.6.57 1 1 0 0 1 1 1V20a1 1 0 0 1-1 1A17 17 0 0 1 3 4a1 1 0 0 1 1-1h3.5a1 1 0 0 1 1 1c0 1.25.2 2.45.57 3.57a1 1 0 0 1-.25 1z"/></svg>
        <span>(555) 014-2200</span>
      </div>
      <div class="contact__row">
        <svg viewBox="0 0 24 24"><path d="M6 2h12v5H6zM4 8h16a2 2 0 0 1 2 2v7h-4v5H6v-5H2v-7a2 2 0 0 1 2-2zm4 8v4h8v-4zm-1-5v2h4v-2z"/></svg>
        <span>(555) 014-2210</span>
      </div>
      <div class="contact__row">
        <svg viewBox="0 0 24 24"><path d="M2 5h20v14H2zm2 2v.5l8 5.5 8-5.5V7zm0 3v7h16v-7l-8 5.5z"/></svg>
        <span>hello@maplegrovedental.com</span>
      </div>
      <div class="contact__row contact__row--addr">
        <svg viewBox="0 0 24 24"><path d="M12 2a7 7 0 0 0-7 7c0 5.2 7 13 7 13s7-7.8 7-13a7 7 0 0 0-7-7zm0 9.5A2.5 2.5 0 1 1 12 6.5a2.5 2.5 0 0 1 0 5z"/></svg>
        <span>48 Brookside Avenue, Suite 210 Fairhaven, CT<br>06000</span>
      </div>
    </div>
    <div class="map" role="img" aria-label="Street map showing the practice location and nearby roads and parks"></div>
  </section>
</body>
</html>
```